Summer Sunglass offer

Need a poster design for a spring / summer campaign. We are an opticians with good footfall. The design needs to be eye catching and aimed at 40 year old plus. The offer is Up to 50% off sunglass offer, t&c apply. (I have attached our last year campaign)
Also need a 2 sided A5 leaflet design (see attached)
I've uploaded a copy of our logo

A5 leaflet should read:

Grab a bargain on two great looks this summer Upto 50% off sunglasses
Look great and stay safe in the sun this summer

We want you to look great, feel fantastic and most of all stay safe in the sun this summer. That’s why we’re offering you 50% off prescription sunglasses with every complete pair of glasses you buy this summer or 25% off for prescription sunglasses with no other purchase.
Find you new summer looks from our gorgeous collection of frames in store. It matters to us that you look great in your new glasses as much as how well you see through them, so we’ll be on hand to help you find frames that suit you best.
What new looks will you go for? Smart or sassy? Formal or Fun? Whatever you’re in the mood for, you’ll find it in our collections this summer.
Call in today to find your new looks, and remember to bring your prescription if you don’t need an eye test.

Target Market(s)

40 + year old

Industry/Entity Type

Optician

Colors

Designer to choose colors to be used in the design.

Requirements
Must have
• Images, preferably a male and Female image

```html
<!DOCTYPE html>
<html lang="en">
<head>
<meta charset="utf-8">
<title>Harwood Eyecare Centre – Up to 50% Off Sunglasses</title>
<link href="https://fonts.googleapis.com/css2?family=Lato:wght@300;400;700;900&display=swap" rel="stylesheet">
<style>
  :root{
    --sky-deep:#27a7c8;
    --sky-light:#7ccbe0;
    --teal:#38b2cb;
    --ring:#5cc3c4;
    --royal:#2b56a6;
    --ink:#2b2b2b;
    --white:#ffffff;
    --sand:#f1efec;
    --pink:#eab6d6;
  }
  *{margin:0;padding:0;box-sizing:border-box}
  html,body{width:846px;height:1200px;overflow:hidden;background:var(--white)}
  body{font-family:"Lato",sans-serif;color:var(--ink)}
  .poster{position:relative;width:846px;height:1200px;overflow:hidden;background:var(--white)}

  .hero{position:absolute;left:0;top:0;width:846px;height:573px;
    background:linear-gradient(120deg,var(--sky-deep) 0%,#5bbfda 45%,var(--sky-light) 100%)}
  .hero-photo{position:absolute;right:0;top:0;width:450px;height:573px;
    background:radial-gradient(ellipse at 55% 40%,#e9c48f 0%,#d98a4a 28%,#e8b846 55%,rgba(124,203,224,0) 80%)}
  .hero-rule{position:absolute;left:0;top:573px;width:846px;height:10px;background:var(--royal)}

  .brand-tab{position:absolute;left:34px;top:0;width:374px;height:102px;background:var(--white);
    border-radius:0 0 30px 30px;display:flex;align-items:center;gap:14px;padding-left:38px}
  .brand-dot{width:34px;height:34px;border-radius:50%;background:var(--teal);flex:none}
  .brand-name{font-weight:700;font-size:21px;line-height:1.15;letter-spacing:2px;color:var(--royal)}

  .headline{position:absolute;left:34px;top:128px;width:390px;color:var(--white)}
  .headline .line-light{font-weight:300;font-size:38px;line-height:48px;letter-spacing:.5px}
  .headline .line-wide{font-weight:900;font-size:37px;line-height:50px;letter-spacing:2.5px}
  .headline .line-tight{font-weight:900;font-size:36px;line-height:50px;letter-spacing:-.5px}
  .headline .strap{font-weight:400;font-size:18px;margin-top:10px;white-space:nowrap}

  .floral{position:absolute;border-radius:50%;
    background:radial-gradient(circle,var(--pink) 0%,#f3d4e6 45%,rgba(170,220,200,.6) 70%,rgba(255,255,255,0) 100%)}
  .floral-left{left:32px;top:350px;width:110px;height:170px}
  .floral-right{left:300px;top:390px;width:90px;height:125px}

  .badge{position:absolute;left:104px;top:331px;width:220px;height:220px;border-radius:50%;background:var(--white);
    display:flex;align-items:center;justify-content:center}
  .badge-ring{position:absolute;inset:10px;border:4px solid var(--ring);border-radius:50%}
  .badge-text{text-align:center;color:var(--royal);font-weight:900;position:relative}
  .badge-text .small{font-size:22px;line-height:26px;letter-spacing:.5px}
  .badge-text .big{font-size:50px;line-height:54px;letter-spacing:-1px}
  .badge-text .label{font-size:25px;line-height:28px;letter-spacing:-.6px}

  .beach{position:absolute;left:0;top:583px;width:846px;height:617px;
    background:radial-gradient(ellipse at 60% 85%,rgba(150,140,135,.22) 0%,rgba(200,195,190,.15) 35%,rgba(255,255,255,0) 70%),
    linear-gradient(180deg,var(--white) 0%,var(--white) 40%,var(--sand) 100%)}

  .copy{position:absolute;left:71px;top:615px;width:708px;font-size:18.5px;line-height:29px}
  .copy p{margin-bottom:13px}
  .copy .justify{text-align:justify;text-align-last:left}
  .copy .cta{color:var(--royal);font-weight:700;font-size:21px;line-height:33px}

  .web-bar{position:absolute;left:72px;top:1051px;width:696px;height:51px;background:var(--teal);
    color:var(--white);font-weight:700;font-size:28px;display:flex;align-items:center;justify-content:center}
  .edge-block{position:absolute;top:1051px;width:51px;height:51px;background:var(--royal)}
  .edge-left{left:0}
  .edge-right{right:0}

  .terms{position:absolute;left:78px;top:1117px;width:685px;font-size:13px;line-height:25px;letter-spacing:.3px}
  .terms span{display:block}
  .terms .first{text-align:justify;text-align-last:justify}
</style>
</head>
<body>
<main class="poster">
  <section class="hero">
    <div class="hero-photo" role="img" aria-label="Smiling woman in a straw sun hat, dark sunglasses and a yellow top against a blue sky"></div>

    <div class="brand-tab">
      <span class="brand-dot"></span>
      <span class="brand-name">HARWOOD<br>EYECARE CENTRE</span>
    </div>

    <div class="headline">
      <div class="line-light">GRAB A BARGAIN ON</div>
      <div class="line-wide">TWO GREAT LOOKS</div>
      <div class="line-tight">THIS SUMMER.</div>
      <div class="strap">Look great and stay safe in the sun this summer</div>
    </div>

    <div class="floral floral-left" role="img" aria-label="Watercolour pink flower and leaves"></div>
    <div class="floral floral-right" role="img" aria-label="Watercolour pink flower and leaves"></div>

    <div class="badge">
      <div class="badge-ring"></div>
      <div class="badge-text">
        <div class="small">UP TO</div>
        <div class="big">50% OFF</div>
        <div class="label">SUNGLASSES</div>
      </div>
    </div>
  </section>
  <div class="hero-rule"></div>

  <div class="beach" role="img" aria-label="Faded photo of sunglasses resting on sand"></div>

  <section class="copy">
    <p>We want you to look great, feel fantastic and most of all stay safe in the sun this summer. That’s why we’re offering you 50% off prescription sunglasses with every complete pair of glasses you buy this summer or 25% off for prescription sunglasses with no other purchase.</p>
    <p class="justify">Find your new summer looks from our gorgeous collection of frames in store. It matters to us that you look great in your new glasses as much as how well you see through them, so we’ll be on hand to help you find frames that suit you best.</p>
    <p>What new looks will you go for? Smart or sassy? Formal or Fun? Whatever you’re in the mood for, you’ll find it in our collections this summer.</p>
    <p class="cta">Call in today to find your new looks, and remember to bring your prescription if you don’t need an eye test.</p>
  </section>

  <div class="edge-block edge-left"></div>
  <div class="web-bar">www.harwoodeyecare.co.uk</div>
  <div class="edge-block edge-right"></div>

  <p class="terms"><span class="first">*Offer includes frame from selected range, standard single vision lenses, tint and uv protection.</span><span>Lens upgrades available at extra cost. Offer excludes Coral Bay frames. Cannot be used with any other offer.</span></p>
</main>
</body>
</html>
```